Desk Allies Business Card

Contact Information for Business Card

Jaakko Virtanola
Managing Director

3/47 Darrow Lane Belmont ACT 2915

Tel: +61 02 6187 4326
Mob: +61 0432 715 649

Email: jaakko@deskallies-example.com.au
Web: www.deskallies-example.com.au

Colors

Designer to choose colors to be used in the design.

Requirements
Must have
• Logo, Name, Title, Address, Telephone, Mobile, Email Address and Website
• "Desk Ally Worldwide Pty Ltd"

```html
<!DOCTYPE html>
<html lang="en">
<head>
<meta charset="utf-8">
<title>Desk Allies Business Card</title>
<link rel="stylesheet" href="https://fonts.googleapis.com/css2?family=Montserrat:wght@400;600&family=Roboto+Condensed:wght@400;700&display=swap">
<style>
  :root {
    --brand-blue: #1f78c8;
    --ink-black: #1e1f21;
    --card-white: #ffffff;
    --text-grey: #5d6166;
    --stage: #2c3034;
  }
  * { box-sizing: border-box; margin: 0; padding: 0; }
  html, body {
    width: 1200px; height: 900px; overflow: hidden;
    background: var(--stage);
  }
  .card {
    position: absolute;
    width: 520px; height: 300px;
    border-radius: 22px;
    overflow: hidden;
    background: var(--card-white);
    box-shadow: 0 10px 30px rgba(0,0,0,.35);
  }
  .card--front { left: 60px; top: 300px; }
  .card--back { left: 620px; top: 300px; }

  .card-bands { position: absolute; inset: 0; }

  .brand {
    position: absolute; left: 30px; top: 28px;
    display: flex; align-items: center; gap: 12px;
  }
  .brand-dot {
    width: 40px; height: 40px; border-radius: 50%;
    background: var(--brand-blue);
  }
  .brand-name {
    font-family: 'Montserrat', sans-serif;
    font-weight: 600; font-size: 36px; line-height: 1;
    color: var(--brand-blue); letter-spacing: 0.5px;
  }
  .brand-tagline {
    position: absolute; left: 82px; top: 72px;
    font-family: 'Montserrat', sans-serif;
    font-weight: 400; font-size: 11.5px; letter-spacing: 3.2px;
    color: var(--text-grey);
  }

  .person {
    position: absolute; left: 30px; top: 112px;
    font-family: 'Roboto Condensed', sans-serif;
  }
  .person-name { font-weight: 700; font-size: 19px; color: var(--ink-black); }
  .person-name .surname { color: var(--brand-blue); }
  .person-title { font-size: 14px; color: var(--ink-black); margin-top: 2px; }

  .contact-online {
    position: absolute; left: 262px; top: 138px;
    font-family: 'Roboto Condensed', sans-serif;
    font-size: 14px; color: var(--ink-black);
    list-style: none;
  }
  .contact-online li, .contact-phones li {
    display: flex; align-items: center; gap: 7px; line-height: 22px;
  }
  .contact-online svg { fill: var(--brand-blue); }

  .contact-phones {
    position: absolute; left: 26px; top: 226px;
    font-family: 'Roboto Condensed', sans-serif;
    font-size: 14px; color: var(--card-white);
    list-style: none;
  }
  .contact-phones svg { fill: var(--card-white); }

  .company {
    position: absolute; left: 226px; top: 236px;
    font-family: 'Roboto Condensed', sans-serif;
    color: var(--card-white); font-size: 15px; line-height: 20px;
  }
  .company-name { font-weight: 700; }

  .back-brand {
    position: absolute; left: 0; right: 0; top: 126px;
    text-align: center;
    font-family: 'Montserrat', sans-serif;
    font-weight: 600; font-size: 46px; line-height: 1;
    color: var(--brand-blue);
  }
</style>
</head>
<body>

<section class="card card--front" aria-label="Business card front">
  <svg class="card-bands" viewBox="0 0 520 300" width="520" height="300" aria-hidden="true">
    <rect x="0" y="208" width="520" height="92" fill="var(--ink-black)"/>
    <path d="M520 200 H218 C196 200 196 222 196 236 V300 H520 Z" fill="var(--brand-blue)"/>
  </svg>

  <div class="brand">
    <span class="brand-dot"></span>
    <span class="brand-name">DESK ALLIES</span>
  </div>
  <div class="brand-tagline">ERGONOMIC OFFICE ENVIRONMENTS</div>

  <div class="person">
    <div class="person-name">JAAKKO <span class="surname">VIRTANOLA</span></div>
    <div class="person-title">Managing Director</div>
  </div>

  <ul class="contact-online">
    <li>
      <svg width="13" height="10" viewBox="0 0 13 10"><path d="M0 0h13v10H0z M1 1l5.5 4.5L12 1"/></svg>
      jaakko@deskallies-example.com.au
    </li>
    <li>
      <svg width="13" height="13" viewBox="0 0 13 13"><circle cx="6.5" cy="6.5" r="6.5"/></svg>
      www.deskallies-example.com.au
    </li>
  </ul>

  <ul class="contact-phones">
    <li>
      <svg width="11" height="12" viewBox="0 0 11 12"><path d="M2 0l2 3-1.3 1.5c.8 1.8 2 3 3.8 3.8L8 7l3 2-1.5 3C5 12 0 7 0 1.5z"/></svg>
      +61 02 6187 4326
    </li>
    <li>
      <svg width="11" height="13" viewBox="0 0 11 13"><path d="M1 0h9v13H1z M2 1.5v9h7v-9z" fill-rule="evenodd"/></svg>
      +61 0432 715 649
    </li>
  </ul>

  <div class="company">
    <div class="company-name">Desk Ally Worldwide Pty Ltd</div>
    <div class="company-address">3/47 Darrow Lane Belmont ACT 2915</div>
  </div>
</section>

<section class="card card--back" aria-label="Business card back">
  <svg class="card-bands" viewBox="0 0 520 300" width="520" height="300" aria-hidden="true">
    <rect x="0" y="0" width="520" height="300" fill="var(--ink-black)"/>
    <path d="M0 0 H300 L120 300 H0 Z" fill="var(--brand-blue)"/>
    <circle cx="270" cy="150" r="205" fill="var(--card-white)"/>
  </svg>
  <div class="back-brand">DESK ALLIES</div>
</section>

</body>
</html>
```